Local Self Storage Company needs a namecard

We need to have a namecard designed out based on the attached logo.

to have a very simple yet modern namecard design to show to others that we are a company that provides self storage and event logistics

Design to be in the format of Ai, PSD and Jpeg when selected

Target Market(s)

customers who are moving house or office
companies that need to have bigger spaces for storage
both for short term or long term

Industry/Entity Type

Self Storage

Requirements
Must have
• The front of the namecard to just have the logo and tag line

The back of the namecard to input the information as:
XX (Name)
XXX (Title)
XX(Hp)
41 Crestmoor Lane, Velmar Industrial Building,
#03-09 Singapore 512694

```html
<!DOCTYPE html>
<html lang="en">
<head>
<meta charset="utf-8">
<title>KEEPVAULT Name Card</title>
<link rel="stylesheet" href="https://fonts.googleapis.com/css2?family=Open+Sans:wght@400;600&display=swap">
<style>
  :root {
    --page-bg: #ecebe8;
    --card-white: #ffffff;
    --card-fade: #d9dadb;
    --charcoal: #4b4c4c;
    --brand-green: #7cc242;
    --brand-blue: #1f4fa3;
    --ink-grey: #6d6e70;
    --text-light: #ffffff;
  }
  * { margin: 0; padding: 0; box-sizing: border-box; }
  html, body {
    width: 1200px;
    height: 1159px;
    overflow: hidden;
    background: var(--page-bg);
    font-family: "Open Sans", Arial, sans-serif;
  }
  .canvas { position: relative; width: 1200px; height: 1159px; }

  .card {
    position: absolute;
    width: 708px;
    height: 409px;
    overflow: hidden;
    box-shadow: 0 10px 24px rgba(0,0,0,0.22);
  }

  /* Front */
  .card-front {
    left: 133px;
    top: 149px;
    background: linear-gradient(to bottom, var(--card-white) 45%, var(--card-fade) 100%);
  }
  .brand-mark {
    position: absolute;
    left: 100px;
    top: 108px;
    width: 166px;
    height: 166px;
    border-radius: 50%;
    background: var(--brand-green);
  }
  .brand-name {
    position: absolute;
    left: 296px;
    top: 168px;
    font-size: 40px;
    font-weight: 600;
    line-height: 1;
    letter-spacing: 1px;
    color: var(--brand-green);
  }
  .brand-tagline {
    position: absolute;
    left: 298px;
    top: 216px;
    font-size: 12px;
    letter-spacing: 4.2px;
    color: var(--ink-grey);
    text-transform: uppercase;
  }
  .front-rule {
    position: absolute;
    left: 87px;
    top: 345px;
    width: 541px;
    height: 3px;
    background: var(--brand-green);
  }

  /* Back */
  .card-back {
    left: 368px;
    top: 607px;
    background: var(--charcoal);
  }
  .back-mark {
    position: absolute;
    left: 75px;
    top: 68px;
    width: 176px;
    height: 176px;
    border-radius: 50%;
    background: var(--brand-green);
  }
  .person {
    position: absolute;
    right: 27px;
    top: 80px;
    text-align: right;
    color: var(--text-light);
    font-size: 35px;
    line-height: 44px;
  }
  .contact-band {
    position: absolute;
    left: 0;
    bottom: 0;
    width: 100%;
    height: 132px;
    background: var(--brand-green);
  }
  .contact-tab {
    position: absolute;
    left: 385px;
    top: 257px;
    width: 271px;
    height: 40px;
    border-radius: 16px 16px 0 0;
    background: var(--brand-green);
  }
  .address {
    position: absolute;
    right: 27px;
    top: 292px;
    text-align: right;
    color: var(--text-light);
    font-size: 21px;
    line-height: 29px;
  }
  .website {
    position: absolute;
    left: 205px;
    top: 364px;
    color: var(--text-light);
    font-size: 26px;
    line-height: 32px;
  }
</style>
</head>
<body>
<main class="canvas">
  <section class="card card-front" aria-label="Name card front">
    <div class="brand-mark"></div>
    <div class="brand-name">KEEPVAULT</div>
    <div class="brand-tagline">Your Storage Solution</div>
    <div class="front-rule"></div>
  </section>

  <section class="card card-back" aria-label="Name card back">
    <div class="back-mark"></div>
    <div class="person">
      <p class="person-name">Daniel Wren</p>
      <p class="person-title">Co-founder</p>
    </div>
    <div class="contact-tab"></div>
    <div class="contact-band"></div>
    <address class="address" style="font-style:normal">
      41 Crestmoor Lane, Velmar Industrial Building,<br>
      #03-09 Singapore 512694
    </address>
    <p class="website">www.keepvault-storage.com</p>
  </section>
</main>
</body>
</html>
```